childcare program (nursery, preschool, pre-k, and afterschool)

Please, make my website WAY better: brightmeadowkids.org.
I'm looking for something clean, simple, but impactful that says, "We love child care, because after 20 years, we really do!" Basically, a website that peaks your interest enough to bring you child to. We serve newborns to 12 yr olds, If you take a look at the website you can get an idea of what we use to attract the different age groups. Please be aware that I am open to suggestions.

Target Market(s)

Parents of newborn to 12 year olds

Industry/Entity Type

Childcare

Coding

Coded - Design and coding required

Number of Pages Required

5+ page

Requirements
Must have
• An upgrade to our website that nothing short of an overhaul.
Id like to have an option to have current customers login to pay their tuition. Link to our Chirpbook.
Nice to have
• Something Innovative and different, up to date features in web design.
Something fun and interactive. Think Bramwick from Tollivar or Pella Vane from Oren Quill. Also, Testimonials
Should not have
• Traditional, boring

```html
<!DOCTYPE html>
<html lang="en">
<head>
<meta charset="utf-8">
<title>Bright Meadow Childcare</title>
<link href="https://fonts.googleapis.com/css2?family=Lato:ital,wght@0,400;0,700;0,900;1,900&display=swap" rel="stylesheet">
<style>
:root{
  --navy:#0b2c47;
  --teal:#2bb5ad;
  --pink:#e8114f;
  --gray:#5d5d5d;
  --ink:#222a33;
  --white:#ffffff;
  --line:#d4d4d4;
}
*{box-sizing:border-box;margin:0;padding:0}
html,body{width:1200px;height:4762px;overflow:hidden;background:var(--white)}
body{font-family:'Lato',sans-serif;color:var(--ink)}
.page{position:relative;width:1200px;height:4762px;overflow:hidden}
.abs{position:absolute}
h2{font-family:'Lato',sans-serif;font-weight:900;color:var(--navy);letter-spacing:.5px}
p{line-height:1.9}
.btn{position:absolute;display:flex;align-items:center;justify-content:center;border-radius:22px;font-size:14px;font-weight:700;letter-spacing:.5px;text-decoration:none}
.btn-teal{background:var(--teal);color:var(--white)}
.btn-pink{background:var(--pink);color:var(--white)}
.btn-outline{border:2px solid var(--pink);color:var(--pink);background:var(--white)}

/* header */
.site-header{position:absolute;top:0;left:0;width:1200px;height:96px;background:var(--white);z-index:5}
.nav-link{position:absolute;top:38px;font-size:14px;font-weight:700;color:var(--navy);text-decoration:none;letter-spacing:.3px}
.nav-home{top:30px;left:74px;width:105px;height:40px;background:var(--pink);color:var(--white);border-radius:20px;display:flex;align-items:center;justify-content:center}
.brand-badge{position:absolute;left:494px;top:-10px;width:214px;height:214px;border-radius:50%;background:var(--white);display:flex;flex-direction:column;align-items:center;justify-content:center;z-index:6;box-shadow:0 2px 6px rgba(0,0,0,.08)}
.brand-dot{width:64px;height:64px;border-radius:50%;background:var(--navy);margin-bottom:10px}
.brand-name{font-size:19px;font-weight:900;color:var(--teal);text-align:center;line-height:1.15}

/* hero */
.hero-photo{position:absolute;top:96px;left:0;width:1200px;height:790px;background:linear-gradient(180deg,#8d8f8a 0%,#5e6a63 45%,#3c4440 100%)}
.hero-title{position:absolute;top:328px;left:0;width:1200px;text-align:center;font-weight:900;font-size:45px;line-height:52px;color:var(--white);text-shadow:0 2px 6px rgba(0,0,0,.35)}
.hero-dots{position:absolute;top:632px;left:560px;display:flex;gap:10px}
.hero-dots span{width:12px;height:12px;border-radius:50%;background:var(--teal)}
.hero-dots span:first-child{background:var(--pink)}
.hero-wave{position:absolute;top:660px;left:0}

/* mission */
.mission-title{top:920px;left:74px;font-size:52px}
.mission-text{top:1000px;left:76px;width:530px;font-size:13.5px;line-height:25px}
.value-card{position:absolute;width:152px;height:137px;border:1.5px solid var(--line);background:var(--white);display:flex;flex-direction:column;align-items:center;justify-content:flex-end;padding-bottom:14px;font-size:16px;font-weight:700;color:var(--ink);text-align:center;line-height:1.2}
.value-card svg{margin-bottom:10px}
.mission-photo{position:absolute;left:698px;top:940px;width:386px;height:386px;border-radius:50%;background:radial-gradient(circle at 50% 55%,#cde63a 0%,#9bb52a 45%,#3a3450 100%)}

/* what we do */
.whatwedo-bg{position:absolute;top:1490px;left:0}
.whatwedo-title{top:1680px;left:634px;font-size:52px;color:var(--white)}
.whatwedo-text{top:1762px;left:635px;width:490px;font-size:13.5px;line-height:25px;color:var(--white)}
.see-label{position:absolute;top:2030px;left:616px;font-size:22px;font-weight:700;color:var(--white)}
.video-thumb{position:absolute;left:828px;top:2008px;width:298px;height:187px;border-radius:8px;background:linear-gradient(120deg,#c9a0d8 0%,#e3b2c6 40%,#9cc0e6 100%);box-shadow:0 4px 10px rgba(0,0,0,.35)}
.play{position:absolute;left:124px;top:68px;width:52px;height:52px;border-radius:50%;background:var(--pink);display:flex;align-items:center;justify-content:center}

/* programs */
.programs-title{top:2290px;left:72px;font-size:52px}
.programs-sub{top:2370px;left:75px;font-size:14px}
.program-ring{position:absolute;width:222px;height:222px;border-radius:50%;border:12px solid var(--navy);border-right-color:var(--teal);border-bottom-color:var(--teal);transform:rotate(20deg)}
.program-photo{position:absolute;width:176px;height:176px;border-radius:50%}
.program-name{position:absolute;font-size:26px;font-weight:900;color:var(--navy)}
.program-text{position:absolute;width:270px;font-size:13.5px;line-height:27px}

/* summer camp */
.camp-bg{position:absolute;top:2995px;left:0}
.camp-title{top:3170px;left:74px;font-size:52px;color:var(--white)}
.camp-quote{position:absolute;top:3258px;left:74px;font-size:31px;font-weight:900;font-style:italic;color:var(--teal);line-height:40px}
.camp-text{top:3355px;left:76px;width:500px;font-size:13.5px;line-height:25px;color:var(--white)}
.camp-photo{position:absolute;left:616px;top:3069px}

/* questions / covid */
.questions-art{position:absolute;left:74px;top:3812px;width:205px;height:185px;border-radius:50%;background:radial-gradient(circle,#dfe8d0 0%,#c7d8b2 60%,rgba(255,255,255,0) 72%)}
.q-title{top:3800px;left:296px;font-size:37px;line-height:40px}
.q-text{top:3900px;left:297px;width:300px;font-size:13.5px;line-height:25px}
.divider{position:absolute;left:615px;top:3810px;width:1.5px;height:238px;background:var(--line)}
.covid-title{top:3802px;left:679px;font-size:37px}
.covid-text{top:3865px;left:680px;width:420px;font-size:13.5px;line-height:25px}

/* testimonials */
.testimonial-bg{position:absolute;top:4095px;left:0}
.testimonial-title{top:4280px;left:74px;font-size:52px;color:var(--white)}
.t-dots{position:absolute;top:4366px;left:222px;display:flex;gap:14px}
.t-dots span{width:12px;height:12px;border-radius:50%;background:var(--white)}
.t-dots span:first-child{background:var(--navy)}
.avatar{position:absolute;left:524px;top:4240px;width:148px;height:148px;border-radius:50%;border:4px solid var(--white);background:radial-gradient(circle at 50% 40%,#7a4a34 0%,#4a2c22 70%)}
.quote{position:absolute;top:4240px;left:706px;width:420px;font-size:15px;line-height:31px;color:var(--white)}
.quote-name{position:absolute;top:4372px;left:706px;font-size:15px;font-weight:900;color:var(--navy)}

/* call band + footer */
.call-band{position:absolute;top:4475px;left:0;width:1200px;height:111px;background:var(--pink);display:flex;align-items:center;justify-content:center;font-size:22px;font-weight:900;color:var(--white)}
.site-footer{position:absolute;top:4586px;left:0;width:1200px;height:176px;background:var(--navy);color:var(--white)}
.footer-nav{position:absolute;top:42px;left:0;width:1200px;display:flex;justify-content:center;gap:48px;font-size:14px;font-weight:700}
.copyright{position:absolute;top:80px;width:1200px;text-align:center;font-size:13px}
.social{position:absolute;top:112px;left:0;width:1200px;display:flex;justify-content:center;gap:18px;font-size:12px;font-weight:700}
</style>
</head>
<body>
<div class="page">

  <header class="site-header">
    <a class="nav-link nav-home">HOME</a>
    <a class="nav-link" style="left:200px">MISSION</a>
    <a class="nav-link" style="left:312px">PROGRAMS</a>
    <a class="nav-link" style="left:810px">GALLERY</a>
    <a class="nav-link" style="left:925px">VIDEOS</a>
    <a class="nav-link" style="left:1030px">CONTACT US</a>
  </header>
  <div class="brand-badge"><span class="brand-dot"></span><span class="brand-name">Bright Meadow<br>Childcare</span></div>

  <section class="hero">
    <div class="hero-photo" role="img" aria-label="Group of cheerful children with balloons and face paint at an outdoor party"></div>
    <h1 class="hero-title">WE LOVE CHILD CARE, BECAUSE AFTER<br>20 YEARS, WE REALLY DO!</h1>
    <div class="hero-dots"><span></span><span></span><span></span><span></span></div>
    <svg class="hero-wave" width="1200" height="320" viewBox="0 0 1200 320">
      <path d="M0 110 C40 175 120 190 230 180 C330 170 420 150 470 132 L470 320 L0 320 Z" fill="#fff"/>
      <path d="M470 132 C560 60 690 40 820 52 C960 64 1080 80 1200 90 L1200 320 L470 320 Z" fill="#fff"/>
      <path d="M470 132 C530 110 560 80 640 58 C760 26 900 60 1000 70 C1100 80 1170 60 1200 56 L1200 226 C1120 262 1030 300 930 300 C800 300 680 240 570 180 C530 160 490 140 470 132 Z" fill="var(--teal)"/>
    </svg>
  </section>

  <section class="mission">
    <h2 class="abs mission-title">OUR MISSION</h2>
    <p class="abs mission-text">We believe that every child is unique and we believe that success and growth come from encouragement and praise. Our teachers focus on building every child's self esteem and confidence through P.A.U.S.E:</p>
    <div class="value-card" style="left:74px;top:1104px">
      <svg width="56" height="56" viewBox="0 0 56 56" fill="none" stroke="var(--navy)" stroke-width="2"><path d="M6 50h44M14 50V36h10v14M32 50V24h10v26"/><circle cx="40" cy="10" r="4"/></svg>Physical Play</div>
    <div class="value-card" style="left:253px;top:1104px">
      <svg width="56" height="56" viewBox="0 0 56 56" fill="none" stroke="var(--navy)" stroke-width="2"><path d="M8 50V22l20-12 20 12v28zM8 50h40M18 28h6v6h-6zM32 28h6v6h-6zM24 40h8v10h-8z"/></svg>Academia</div>
    <div class="value-card" style="left:433px;top:1104px">
      <svg width="56" height="56" viewBox="0 0 56 56" fill="none" stroke="var(--navy)" stroke-width="2"><circle cx="18" cy="18" r="5"/><circle cx="38" cy="18" r="5"/><path d="M10 50V30h16v20M30 50V30h16v20"/></svg>Unconditional<br>Love</div>
    <div class="value-card" style="left:74px;top:1265px">
      <svg width="56" height="56" viewBox="0 0 56 56" fill="none" stroke="var(--navy)" stroke-width="2"><path d="M28 6l16 6v12c0 10-7 17-16 20-9-3-16-10-16-20V12z"/><path d="M28 16v14M21 23h14"/></svg>Safety</div>
    <div class="value-card" style="left:253px;top:1265px">
      <svg width="56" height="56" viewBox="0 0 56 56" fill="none" stroke="var(--navy)" stroke-width="2"><rect x="12" y="8" width="30" height="40" rx="2"/><path d="M18 18h18M18 26h18M18 34h12M8 50h40"/></svg>Edification</div>

    <svg class="abs" style="left:618px;top:860px" width="546" height="546" viewBox="0 0 546 546">
      <circle cx="273" cy="273" r="250" fill="none" stroke="var(--navy)" stroke-width="22" stroke-dasharray="620 951" transform="rotate(150 273 273)"/>
      <circle cx="273" cy="273" r="262" fill="none" stroke="var(--gray)" stroke-width="16" stroke-dasharray="560 1086" transform="rotate(-40 273 273)"/>
      <circle cx="273" cy="273" r="218" fill="none" stroke="var(--navy)" stroke-width="8" stroke-dasharray="300 1070" transform="rotate(200 273 273)"/>
    </svg>
    <div class="mission-photo" role="img" aria-label="Children in bright yellow camp shirts sitting together indoors"></div>
  </section>

  <section class="whatwedo">
    <svg class="whatwedo-bg" width="1200" height="754" viewBox="0 0 1200 754">
      <path d="M0 100 C200 110 330 80 500 40 C700 0 900 -10 1050 10 C1120 20 1170 30 1200 40 L1200 754 L0 754 Z" fill="var(--navy)"/>
      <defs><linearGradient id="kidsGrad" x1="0" y1="0" x2="1" y2="1"><stop offset="0" stop-color="#7a6250"/><stop offset=".55" stop-color="#4f8fb8"/><stop offset="1" stop-color="#2a5f86"/></linearGradient></defs>
      <path role="img" aria-label="Smiling caregiver with a boy in face paint" d="M0 100 L390 100 C480 150 560 250 585 380 C600 500 540 660 400 680 C280 695 180 620 100 540 C60 500 20 460 0 440 Z" fill="url(#kidsGrad)"/>
    </svg>
    <h2 class="abs whatwedo-title">WHAT WE DO?</h2>
    <p class="abs whatwedo-text">We strive to provide a safe learning environment that will inspire each child in our care to explore and grow at his or her own pace.<br>Our team of administrators, teachers, and caregivers spend time nurturing your children's strengths while encouraging them<br>to reach new heights.</p>
    <a class="btn btn-teal" style="left:634px;top:1915px;width:132px;height:40px">READ MORE</a>
    <span class="see-label">See for yourself!</span>
    <svg class="abs" style="left:668px;top:2080px" width="124" height="90" viewBox="0 0 124 90" fill="none" stroke="#fff" stroke-width="3" stroke-linecap="round"><path d="M6 6 C20 50 60 72 112 68"/><path d="M90 52 L114 68 L88 82"/></svg>
    <div class="video-thumb" role="img" aria-label="Colourful video cover for the summer camp film">
      <span class="play"><svg width="20" height="22" viewBox="0 0 20 22"><path d="M3 2 L18 11 L3 20 Z" fill="#fff"/></svg></span>
    </div>
  </section>

  <section class="programs">
    <h2 class="abs programs-title">PROGRAMS</h2>
    <p class="abs programs-sub">Click Programsfor a full range of classes that foster your child's individual growth</p>

    <div class="program-ring" style="left:74px;top:2433px"></div>
    <div class="program-photo" style="left:97px;top:2456px;background:linear-gradient(135deg,#c98e6a,#5a3a2a)" role="img" aria-label="Baby held in a parent's arms"></div>
    <h3 class="program-name" style="left:316px;top:2438px">NURSERY</h3>
    <p class="program-text" style="left:316px;top:2476px">We believe that the best place for your baby is in your arms. But being that most homes today contain two "breadwinners"</p>
    <a class="btn btn-outline" style="left:316px;top:2602px;width:134px;height:40px">READ MORE</a>

    <div class="program-ring" style="left:616px;top:2433px"></div>
    <div class="program-photo" style="left:639px;top:2456px;background:linear-gradient(135deg,#e6d2c8,#9a6a58)" role="img" aria-label="Preschool girl playing with a toy"></div>
    <h3 class="program-name" style="left:856px;top:2438px">PRESCHOOLERS</h3>
    <p class="program-text" style="left:856px;top:2476px">As your child grows, so does his curiosity meter. Your toddler absorbs information like a sponge at this stage.</p>
    <a class="btn btn-outline" style="left:856px;top:2602px;width:134px;height:40px">READ MORE</a>

    <div class="program-ring" style="left:74px;top:2703px"></div>
    <div class="program-photo" style="left:97px;top:2726px;background:linear-gradient(135deg,#b9423e,#5a3a3a)" role="img" aria-label="Pre-K children seated in a classroom"></div>
    <h3 class="program-name" style="left:316px;top:2708px">PRE-K</h3>
    <p class="program-text" style="left:316px;top:2746px">Our Pre-Kers never stop exoploring, and are introduced to problem-solving concepts that involve math and science.</p>
    <a class="btn btn-outline" style="left:316px;top:2872px;width:134px;height:40px">READ MORE</a>

    <div class="program-ring" style="left:616px;top:2703px"></div>
    <div class="program-photo" style="left:639px;top:2726px;background:linear-gradient(135deg,#d8b8a4,#6a4a3a)" role="img" aria-label="Boy doing homework at a desk"></div>
    <h3 class="program-name" style="left:856px;top:2708px">AFTER-SCHOOL</h3>
    <p class="program-text" style="left:856px;top:2746px">Our AfterSchoolers know the drill - "Do what we have to do, so we can do what we wanna do.</p>
    <a class="btn btn-outline" style="left:856px;top:2872px;width:134px;height:40px">READ MORE</a>
  </section>

  <section class="camp">
    <svg class="camp-bg" width="1200" height="780" viewBox="0 0 1200 780">
      <path d="M0 0 H1200 V620 C1080 600 960 640 820 690 C640 750 420 760 250 740 C120 725 40 730 0 700 Z" fill="var(--navy)"/>
    </svg>
    <h2 class="abs camp-title">SUMMER CAMP</h2>
    <div class="camp-quote">"Mommy, I'm<br>BrightMeadowCamp!"</div>
    <p class="abs camp-text">At Bright Meadow Summer Camp, your child's summer will be packed with fun-filled learning experiences. Your child will navigate through the universe around them through Field trips to Museums, Farms, and zoos; experience magic shows, cool down at awesome Aquatic Parks, and so much more - and all for an incredible cost!</p>
    <a class="btn btn-teal" style="left:74px;top:3498px;width:134px;height:40px">READ MORE</a>
    <svg class="camp-photo" width="584" height="560" viewBox="0 0 584 560">
      <defs><linearGradient id="campGrad" x1="0" y1="0" x2="0" y2="1"><stop offset="0" stop-color="#6a7a3a"/><stop offset=".5" stop-color="#c9e83a"/><stop offset="1" stop-color="#4a5a6a"/></linearGradient></defs>
      <path role="img" aria-label="Two smiling children in yellow camp shirts outdoors" d="M150 20 C260 -10 420 0 520 40 C560 60 584 90 584 120 L584 520 C500 520 420 540 330 556 C200 570 90 520 40 420 C0 330 -10 220 30 130 C60 70 100 35 150 20 Z" fill="url(#campGrad)"/>
    </svg>
  </section>

  <section class="contact-row">
    <div class="questions-art" role="img" aria-label="Illustration of a shrugging woman with a question mark"></div>
    <h2 class="abs q-title">GOT<br>QUESTIONS?</h2>
    <p class="abs q-text">That's why we're here! Send us a note and we'll be more than happy to answer any questions you may have.</p>
    <a class="btn btn-pink" style="left:300px;top:3996px;width:180px;height:42px">SEND US A NOTE</a>
    <span class="divider"></span>
    <h2 class="abs covid-title">COVID-19 UPDATE</h2>
    <p class="abs covid-text">Lorem ipsum dolor sit amet, consectetur adipiscing elit. Etiam dignissim ut massa in sagittis. Integer at urna sit amet ante fermentum finibus. Phasellus nec est tempor, mollis sem in, vestibulum eros fermentum ipsum.</p>
    <a class="btn btn-pink" style="left:683px;top:3996px;width:180px;height:42px">GET UPDATES</a>
  </section>

  <section class="testimonials">
    <svg class="testimonial-bg" width="1200" height="380" viewBox="0 0 1200 380">
      <path d="M0 50 C150 90 300 100 500 70 C700 40 850 60 980 40 C1080 25 1150 20 1200 28 V380 H0 Z" fill="var(--teal)"/>
    </svg>
    <h2 class="abs testimonial-title">TESTIMONIALS</h2>
    <div class="t-dots"><span></span><span></span><span></span><span></span></div>
    <div class="avatar" role="img" aria-label="Portrait of a smiling parent"></div>
    <p class="quote">"&nbsp; Maecenas venenatis fringilla eleifend ullam dapibus tincidunt augue sed porttitor. Quisque vulputate ex ut ipsum rhoncus tristique. Mauris elit eros, malesuada eu maximus in, tincidunt in dui..."</p>
    <span class="quote-name">NAME HEADING</span>
  </section>

  <div class="call-band">Call Us Today at 5550104822. Three amazing locations to serve you.</div>

  <footer class="site-footer">
    <nav class="footer-nav"><span>HOME</span><span>MISSION</span><span>PROGRAMS</span><span>GALLERY</span><span>VIDEOS</span><span>CONTACT US</span></nav>
    <p class="copyright">Copyright &copy; 2020 Bright Meadow Childcare, Inc All Rights Reserved.</p>
    <div class="social"><span>Chirpbook</span><span>Flitter</span><span>Snapgram</span><span>Linkwise</span><span>Vidtube</span></div>
  </footer>

</div>
</body>
</html>
```